Accounting Firm

We are a two partner accounting firm. our business name is VELLOR & BRISKETT. We are accountants and business consultants.

We need a stationery design for our letterhead, with compliments slip, business card and envelope.

We'd like clean, professional look. I'm 39 years old and my partner is 60+, so we'd like modern yet elegant design. Dark Navy Blue as a primary colour is preferred.

Thank you.

Hi Guys

No logo.

Thanks

Accounting

• Firm name :VELLOR & BRISKETT
Business Consultants & Accountants
Address: Level 2 Units 3 & 4, 27 Marrow Crescent HALDEN SA 5094
Box address: PO Box 318 CARVELL SA 5098
telp: +61 8 8194 6027
fax: +61 8 8456 2719

Dominic Vellor, CA
Lucas Briskett, CPA

dominic.vellor@vellorbriskett.example.au
lucas.briskett@vellorbriskett.example.au

Dark Navy Blue as primary colour

```html
<!DOCTYPE html>
<html lang="en">
<head>
<meta charset="utf-8">
<title>Vellor &amp; Briskett — Stationery Set</title>
<link rel="stylesheet" href="https://fonts.googleapis.com/css2?family=Questrial&family=Arimo:wght@400&display=swap">
<style>
  :root {
    --navy: #05496b;
    --navy-soft: #1d5e7e;
    --charcoal: #3d3d3f;
    --frame: #555;
    --text-grey: #444;
    --paper: #ffffff;
    --sheet: #f7f9fb;
  }
  * { margin: 0; padding: 0; box-sizing: border-box; }
  html, body { width: 849px; height: 1200px; overflow: hidden; background: var(--paper); }
  .canvas { position: relative; width: 849px; height: 1200px; font-family: "Questrial", sans-serif; color: var(--navy); }
  .piece { position: absolute; border: 1px solid var(--frame); background: var(--sheet); }
  .block { position: absolute; }
  .navy { background: var(--navy); }
  .charcoal { background: var(--charcoal); }
  .ornament { position: absolute; background: linear-gradient(90deg, var(--navy-soft), var(--navy)); border-radius: 4px; }
  .ornament.on-white { background: linear-gradient(90deg, #e6eef3, #d3e0e8); }
  .wordmark { position: absolute; line-height: 0.92; color: var(--navy); white-space: nowrap; }
  .tagline { position: absolute; font-family: "Arimo", sans-serif; color: var(--charcoal); white-space: nowrap; }
  .address { position: absolute; font-family: "Questrial", sans-serif; line-height: 1.2; white-space: nowrap; }
  .address.light { color: #fff; }
  .address.dark { color: var(--text-grey); }
  .address .row { display: block; }
  .address .label { display: inline-block; width: 34px; text-align: left; }
  .right { text-align: right; }
  .center { text-align: center; }
  .compliments { position: absolute; font-size: 17px; color: var(--navy); }
  .window { position: absolute; border: 1px solid var(--frame); border-radius: 9px; }
  .recipient { position: absolute; font-size: 13px; line-height: 1.25; color: #222; }
  .card-name { position: absolute; font-size: 10.5px; color: var(--navy); white-space: nowrap; }
  .card-role { position: absolute; font-size: 8px; color: var(--text-grey); white-space: nowrap; }
  .card-contact { position: absolute; font-size: 5.3px; line-height: 1.3; color: var(--text-grey); white-space: nowrap; }
  .card-contact .label { display: inline-block; width: 18px; }
</style>
</head>
<body>
<div class="canvas">

  <!-- Letterhead -->
  <section class="piece letterhead" style="left:116px;top:44px;width:616px;height:90px;">
    <div class="block navy" style="left:1px;top:15px;width:14px;height:45px;"></div>
    <div class="wordmark" style="left:21px;top:13px;font-size:27px;">Vellor<br>&amp; Briskett</div>
    <div class="tagline" style="left:21px;top:70px;font-size:8.5px;">Business Consultants &amp; Accountants</div>
    <div class="block navy" style="left:174px;top:15px;width:442px;height:45px;"></div>
    <div class="ornament" role="img" aria-label="Swirl ornament" style="left:177px;top:19px;width:74px;height:37px;"></div>
    <div class="address light right" style="right:15px;top:19px;font-size:8px;">
      <span class="row">Level 2 Units 3 &amp; 4, 27 Marrow Crescent HALDEN SA 5094</span>
      <span class="row">PO Box 318 CARVELL SA 5098</span>
      <span class="row"><span class="label">phone</span>+61 8 8194 6027</span>
      <span class="row"><span class="label">fax</span>+61 8 8456 2719</span>
    </div>
    <div class="block charcoal" style="left:0;top:67px;width:14px;height:9px;"></div>
    <div class="block charcoal" style="left:174px;top:67px;width:442px;height:9px;"></div>
  </section>

  <!-- Compliments slip -->
  <section class="piece compliments-slip" style="left:177px;top:157px;width:493px;height:222px;">
    <div class="block navy" style="left:1px;top:20px;width:14px;height:46px;"></div>
    <div class="wordmark" style="left:21px;top:18px;font-size:27px;">Vellor<br>&amp; Briskett</div>
    <div class="tagline" style="left:21px;top:77px;font-size:8.5px;">Business Consultants &amp; Accountants</div>
    <div class="block navy" style="left:174px;top:20px;width:319px;height:46px;"></div>
    <div class="ornament" role="img" aria-label="Swirl ornament" style="left:177px;top:24px;width:74px;height:38px;"></div>
    <div class="block charcoal" style="left:0;top:73px;width:14px;height:7px;"></div>
    <div class="block charcoal" style="left:174px;top:73px;width:319px;height:7px;"></div>
    <div class="address dark right" style="right:13px;top:90px;font-size:8px;">
      <span class="row">Level 2 Units 3 &amp; 4, 27 Marrow Crescent HALDEN SA 5094</span>
      <span class="row">PO Box 318 CARVELL SA 5098</span>
      <span class="row"><span class="label">phone</span>+61 8 8194 6027</span>
      <span class="row"><span class="label">fax</span>+61 8 8456 2719</span>
    </div>
    <div class="block navy" style="left:2px;top:176px;width:14px;height:13px;"></div>
    <div class="compliments" style="left:22px;top:171px;">with compliments</div>
    <div class="block charcoal" style="left:0;top:194px;width:493px;height:8px;"></div>
  </section>

  <!-- Envelope front -->
  <section class="piece envelope-front" style="left:102px;top:401px;width:644px;height:282px;">
    <div class="block navy" style="left:0;top:43px;width:15px;height:48px;"></div>
    <div class="wordmark" style="left:20px;top:40px;font-size:29px;">Vellor<br>&amp; Briskett</div>
    <div class="tagline" style="left:20px;top:103px;font-size:9px;">Business Consultants &amp; Accountants</div>
    <div class="block navy" style="left:174px;top:44px;width:470px;height:47px;"></div>
    <div class="ornament" role="img" aria-label="Swirl ornament" style="left:177px;top:48px;width:78px;height:38px;"></div>
    <div class="block charcoal" style="left:0;top:98px;width:15px;height:8px;"></div>
    <div class="block charcoal" style="left:174px;top:98px;width:470px;height:8px;"></div>
    <div class="window" style="left:15px;top:156px;width:232px;height:104px;"></div>
    <div class="recipient" style="left:46px;top:189px;">to Mr. Alfa<br>lorem ipsum dolor sit amet</div>
  </section>

  <!-- Envelope back -->
  <section class="piece envelope-back" style="left:102px;top:705px;width:644px;height:282px;">
    <div class="block navy" style="left:0;top:43px;width:644px;height:47px;"></div>
    <div class="address light center" style="left:0;width:644px;top:49px;font-size:8px;">
      <span class="row">Level 2 Units 3 &amp; 4, 27 Marrow Crescent HALDEN SA 5094</span>
      <span class="row">PO Box 318 CARVELL SA 5098</span>
      <span class="row"><span class="label">phone</span>+61 8 8194 6027</span>
      <span class="row"><span class="label">fax</span>+61 8 8456 2719</span>
    </div>
    <div class="block charcoal" style="left:0;top:97px;width:644px;height:8px;"></div>
  </section>

  <!-- Business card front -->
  <section class="piece card-front" style="left:156px;top:1008px;width:254px;height:146px;">
    <div class="block navy" style="left:0;top:11px;width:157px;height:26px;"></div>
    <div class="ornament" role="img" aria-label="Swirl ornament" style="left:112px;top:14px;width:43px;height:20px;"></div>
    <div class="wordmark" style="left:161px;top:9px;font-size:15.5px;">Vellor<br>&amp; Briskett</div>
    <div class="block navy" style="left:244px;top:11px;width:9px;height:26px;"></div>
    <div class="tagline" style="left:161px;top:40px;font-size:4.5px;">Business Consultants &amp; Accountants</div>
    <div class="block charcoal" style="left:0;top:38px;width:157px;height:4px;"></div>
    <div class="block charcoal" style="left:244px;top:38px;width:9px;height:4px;"></div>
    <div class="card-name" style="left:12px;top:58px;">Lucas Briskett, CPA</div>
    <div class="card-role" style="left:12px;top:73px;">Chief Executive Officer</div>
    <div class="card-contact" style="left:12px;top:92px;">
      lucas.briskett@vellorbriskett.example.au<br>
      Level 2 Units 3 &amp; 4, 27 Marrow Crescent HALDEN SA 5094<br>
      PO Box 318 CARVELL SA 5098<br>
      <span class="label">phone</span>+61 8 8194 6027<br>
      <span class="label">fax</span>+61 8 8456 2719
    </div>
    <div class="ornament on-white" role="img" aria-label="Swirl ornament" style="left:194px;top:97px;width:58px;height:35px;"></div>
    <div class="block charcoal" style="left:0;top:133px;width:253px;height:4px;"></div>
  </section>

  <!-- Business card back -->
  <section class="piece card-back" style="left:437px;top:1008px;width:255px;height:146px;">
    <div class="block navy" style="left:0;top:56px;width:84px;height:25px;"></div>
    <div class="ornament" role="img" aria-label="Swirl ornament" style="left:48px;top:59px;width:34px;height:19px;"></div>
    <div class="wordmark" style="left:87px;top:54px;font-size:15.5px;">Vellor<br>&amp; Briskett</div>
    <div class="block navy" style="left:175px;top:56px;width:80px;height:25px;"></div>
    <div class="ornament" role="img" aria-label="Swirl ornament" style="left:178px;top:59px;width:40px;height:19px;"></div>
    <div class="block charcoal" style="left:0;top:84px;width:84px;height:4px;"></div>
    <div class="block charcoal" style="left:175px;top:84px;width:80px;height:4px;"></div>
    <div class="tagline" style="left:87px;top:86px;font-size:4.5px;">Business Consultants &amp; Accountants</div>
  </section>

</div>
</body>
</html>
```